URGENT!! IT Company Needs a Technological Event Design

We need an invitation design for a technological security event we are hosting. The event is about data and application security solutions that protect business-critical information in the cloud and on-premises. I will provide the logos that need to be used and the information of the date, place and time. The invitation has to be in Spanish.
Updates

Target Market(s)

This event is for high profile clients, therefore, the invite should be innovative and referring to the subject described above and security.

Industry/Entity Type

It Company

Requirements
Must have
• The logos of both companies, and technological concept, regarding data and application security for businesses.
• Fecha (date): Jueves 22 de febrero del 2018
• Lugar (place): Verbena, Av. Las Gardenias.
• Hora (time): 6:30pm

```html
<!DOCTYPE html>
<html lang="es">
<head>
<meta charset="utf-8">
<title>Invitación – Soluciones de Seguridad de Datos y Aplicaciones</title>
<link rel="stylesheet" href="https://fonts.googleapis.com/css2?family=Fira+Sans+Condensed:wght@500;700;800&display=swap">
<style>
  :root {
    --page-bg: #e6e6e6;
    --band-light: #cfe3f1;
    --band-light-2: #a9cde6;
    --body-blue-light: #3b97cf;
    --body-blue: #1f6fb0;
    --body-blue-deep: #15508f;
    --navy: #1b2d5c;
    --brand-blue: #163d7a;
    --brand-grey: #3a3f46;
    --accent-red: #d8342a;
    --white: #ffffff;
  }
  * { box-sizing: border-box; margin: 0; padding: 0; }
  html, body {
    width: 1200px; height: 1000px; overflow: hidden;
    background: var(--page-bg);
    font-family: "Fira Sans Condensed", "Arial Narrow", sans-serif;
  }
  .invitation {
    position: absolute; left: 290px; top: 50px;
    width: 620px; height: 900px;
    background: linear-gradient(160deg, var(--body-blue-light) 0%, var(--body-blue) 55%, var(--body-blue-deep) 100%);
    box-shadow: 0 10px 30px rgba(0,0,0,.25);
    overflow: hidden;
  }
  .tech-backdrop {
    position: absolute; inset: 0;
    background:
      radial-gradient(circle at 50% 52%, rgba(120,190,235,.45) 0%, rgba(120,190,235,.15) 28%, transparent 45%),
      radial-gradient(circle at 10% 30%, rgba(200,230,250,.35) 0%, transparent 30%),
      radial-gradient(circle at 92% 72%, rgba(200,230,250,.35) 0%, transparent 30%);
  }
  .brand-band {
    position: absolute; left: 0; right: 0; top: 0; height: 120px;
    background: linear-gradient(180deg, var(--band-light) 0%, var(--band-light-2) 100%);
    display: flex; align-items: center; justify-content: space-between;
    padding: 0 34px;
  }
  .brand { display: flex; align-items: center; gap: 10px; font-weight: 800; font-size: 36px; letter-spacing: 1px; }
  .brand-mark { width: 28px; height: 28px; border-radius: 50%; flex: none; }
  .brand--host { color: var(--brand-blue); margin-top: 36px; }
  .brand--host .brand-mark { background: var(--brand-blue); }
  .brand--partner { color: var(--brand-grey); margin-top: -30px; }
  .brand--partner .brand-mark { background: var(--accent-red); }
  .event-copy {
    position: absolute; left: 30px; right: 30px; top: 285px;
    text-align: center;
  }
  .event-lead { color: var(--white); font-weight: 700; font-size: 28px; margin-bottom: 12px; }
  .event-title {
    color: var(--navy); font-weight: 800; font-size: 46px; line-height: 1.05;
    text-transform: uppercase;
    text-shadow: 0 0 10px rgba(255,255,255,.9), 0 0 3px rgba(255,255,255,.9);
  }
  .event-date {
    margin-top: 28px; color: var(--white); font-weight: 700;
    font-size: 34px; line-height: 1.1; text-transform: uppercase;
  }
  .details-band {
    position: absolute; left: 0; right: 0; top: 695px; height: 110px;
    background: linear-gradient(90deg, var(--band-light) 0%, var(--band-light-2) 100%);
    color: var(--navy); font-weight: 700; font-size: 20px; text-transform: uppercase;
  }
  .details-place { position: absolute; left: 30px; top: 44px; line-height: 1.3; }
  .details-time { position: absolute; right: 30px; top: 18px; }
</style>
</head>
<body>
  <article class="invitation">
    <div class="tech-backdrop" role="img" aria-label="Fondo tecnológico azul con patrón de puntos y circuitos"></div>

    <header class="brand-band">
      <div class="brand brand--host"><span class="brand-mark"></span>VAULTERA</div>
      <div class="brand brand--partner"><span class="brand-mark"></span>NEXORA</div>
    </header>

    <section class="event-copy">
      <p class="event-lead">Invita al evento</p>
      <h1 class="event-title">Soluciones de seguridad<br>de datos y aplicaciones</h1>
      <p class="event-date">Jueves<br>22 de febrero<br>del 2018</p>
    </section>

    <footer class="details-band">
      <p class="details-place">Lugar:<br>Verbena, Av. Las Gardenias.</p>
      <p class="details-time">Hora: 6:30 p.m.</p>
    </footer>
  </article>
</body>
</html>
```